Redesign B2B website

We are redesigning/ restructuring our current website. We provide company feedback surveys. We claim to be market leader in our country.
We like to be seen as a trustworthy, reliable and innovative partner to the top 1500 companies in the netherlands.
We want to be seen as a personal company.
Current website http://www.brunsvold.nl does not meet our standards mentioned above.
Updates
Added Homepage layout. Please check
Target Market(s)
Large businesses, HR, decisiontakers
Industry/Entity Type
It Company
Requirements
Must have
- -The website is intended to be responsive. please take that into account. (propose plonkav.es)
-The design should match our Style colors(will be provided)
- Wireframes are provided. Fonts used are Open Sans and Esteban,. Feel free to change things around.
Nice to have
- We like the design to be "flat", not much 3d effects, or icons.
Minimalist, Wordpress style or Metro style.

```html
<!DOCTYPE html>
<html lang="nl">
<head>
<meta charset="utf-8">
<title>Brunsvold – Employee and customer surveys</title>
<link rel="stylesheet" href="https://fonts.googleapis.com/css2?family=Open+Sans:ital,wght@0,400;0,600;0,700;1,600;1,700&display=swap">
<style>
:root{
  --navy:#0d4a8e;
  --navy-dark:#0a3a72;
  --brand:#0f5aa3;
  --accent:#f6c51b;
  --date:#e7a10e;
  --text:#3c3c3c;
  --muted:#6a6a6a;
  --rule:#d8d8d8;
  --page:#ffffff;
  --outer:#f1f1f1;
}
*{box-sizing:border-box;margin:0;padding:0}
html,body{width:900px;height:1200px;overflow:hidden}
body{background:var(--outer);font-family:"Open Sans",Arial,sans-serif;color:var(--text);font-size:8.5px;line-height:1.45}
.site{position:absolute;left:77px;top:0;width:746px;height:1200px;background:var(--page)}
.abs{position:absolute}
a{color:inherit;text-decoration:none}

/* header */
.brand-box{left:8px;top:21px;width:235px;height:43px;border:2px solid var(--navy);padding:2px}
.brand-box .inner{width:100%;height:100%;background:var(--navy);display:flex;align-items:center;padding-left:10px;gap:10px}
.brand-name{color:#fff;font-weight:700;font-size:22px;letter-spacing:2px}
.brand-dot{width:22px;height:22px;border-radius:50%;background:#fff}
.top-contact{right:20px;top:12px;display:flex;align-items:center;gap:9px;font-size:9px;color:#333}
.social{display:flex;gap:9px}
.social span{width:14px;height:14px;border-radius:50%;background:#2a2a2a;display:block}

/* nav */
.nav{left:0;top:90px;width:746px;height:28px;background:var(--navy);display:flex;align-items:center;color:#fff;font-size:9.5px}
.nav .item{height:28px;display:flex;align-items:center;justify-content:center;border-right:1px solid var(--navy-dark)}
.nav .active{position:relative;background:var(--accent);color:#222;height:40px;margin-top:-12px;width:70px;margin-left:12px}
.search{margin-left:6px;width:110px;height:18px;border-radius:9px;background:#1a78d6;border:2px solid #0b5bb0;position:relative}
.search svg{position:absolute;right:5px;top:2px}

/* hero */
.hero{left:0;top:118px;width:746px;height:256px;display:flex;gap:6px}
.hero div{height:100%}
.p1{width:183px;background:linear-gradient(160deg,#c9ced3,#5a6470 60%,#2e3338)}
.p2{width:180px;background:linear-gradient(180deg,#f3f4f6,#dfe3e8)}
.p3{width:181px;background:linear-gradient(180deg,#e4e6e8,#3a3c40 70%,#222)}
.p4{width:184px;background:linear-gradient(180deg,#eef3f8,#b9c6d3 70%,#6c7a88)}
.hero-shadow{left:30px;top:374px;width:686px;height:6px;background:radial-gradient(ellipse at top,rgba(0,0,0,.25),transparent 70%)}

/* features */
.features{left:0;top:392px;width:746px;height:207px;border-top:1px dashed var(--rule);border-bottom:1px dashed var(--rule);display:flex}
.feature{position:relative;padding:15px 10px 0 10px;border-right:1px dashed var(--rule)}
.feature:last-child{border-right:none}
.feature h2{font-weight:400;font-size:15.5px;color:#333;margin-bottom:18px}
.feature h2 b{color:var(--brand);font-weight:700}
.lead{display:flex;gap:8px}
.icon{flex:0 0 62px;height:52px;border-radius:4px}
.lead p{text-align:justify}
.lead em{color:var(--brand);font-weight:700}
.feature .body{text-align:justify;margin:10px 6px 0 10px}
.more{position:absolute;right:18px;bottom:6px;font-weight:700;color:#777}
.more.on{color:var(--brand)}

/* trusted */
.trusted{left:13px;top:627px;width:720px;height:72px;border:1px solid #ddd;border-radius:4px;background:linear-gradient(#fff,#f2f2f2)}
.trusted h3{position:absolute;left:14px;top:-12px;background:#fff;padding:0 4px;font-weight:400;font-size:14px;color:#444}
.badges{display:flex;align-items:center;justify-content:space-around;height:100%;padding:0 24px}
.badges span{display:block;background:#4a4a4a}

/* news */
.news{left:0;top:712px;width:746px;height:198px;display:flex;border-bottom:1px dashed var(--rule)}
.col{padding:18px 12px 0 12px}
.col.list{width:250px;border-right:1px dashed var(--rule)}
.col.video{width:260px;border-right:1px dashed var(--rule);padding:20px 23px 0}
.col.tweets{flex:1;padding-top:18px}
.post{padding-left:12px;position:relative;margin-bottom:10px}
.post::before{content:"»";position:absolute;left:0;top:-2px;color:var(--navy);font-weight:700}
.post h4,.tweet h4{font-style:italic;font-weight:700;color:var(--brand);font-size:8.5px;text-align:justify}
.post time{color:var(--date);font-style:normal;font-weight:400}
.tweet{margin-bottom:12px}
.tweet a{color:var(--brand)}
.player{width:210px;height:143px;background:#000;position:relative;color:#ddd;font-size:5.5px}
.player .title{height:11px;background:#2b2b2b;padding:2px 16px;font-weight:700}
.player .bar{position:absolute;left:0;right:0;bottom:0;height:16px;background:#1c1c1c;border-top:2px solid #555;padding:1px 3px}
.player-shadow{width:180px;height:6px;margin:0 auto;background:radial-gradient(ellipse at top,rgba(0,0,0,.3),transparent 70%)}

/* footer */
.contact-bar{left:0;top:914px;width:746px;height:49px;border-bottom:1px dashed var(--rule);display:flex;align-items:center;padding:0 8px;font-size:9px}
.contact-bar .social span{background:#333}
.newsletter{margin-left:auto;display:flex;align-items:center;gap:12px;font-size:9.5px}
.newsletter .field{width:190px;height:24px;border-radius:12px;border:1px solid #ddd;background:#fff;position:relative;box-shadow:inset 0 1px 2px rgba(0,0,0,.08)}
.newsletter svg{position:absolute;right:8px;top:5px}
.sitemap{left:0;top:968px;width:746px;height:170px;display:flex}
.sitemap section{padding:6px 13px 0;border-right:1px solid #ddd;font-size:8.5px}
.sitemap section:last-child{border-right:none}
.sitemap h5{font-weight:400;font-size:13px;color:#444;margin-bottom:12px}
.sitemap h5 b{font-weight:700}
.sitemap li{list-style:none;margin-bottom:4.5px;padding-left:10px;position:relative}
.sitemap li::before{content:"";position:absolute;left:0;top:3px;border-left:4px solid var(--navy);border-top:3px solid transparent;border-bottom:3px solid transparent}
.legal{left:0;top:1153px;width:746px;height:47px;border-top:2px solid #eee;display:flex;align-items:center;justify-content:center;gap:34px;font-size:8.5px;color:#333}
</style>
</head>
<body>
<div class="site">

  <header>
    <div class="abs brand-box"><div class="inner"><span class="brand-name">BRUNSVOLD</span><span class="brand-dot"></span></div></div>
    <div class="abs top-contact">020-41 62 200 - CONTACT
      <div class="social"><span></span><span></span><span></span><span></span></div>
    </div>
  </header>

  <nav class="abs nav">
    <a class="item active">PRODUCTEN</a>
    <a class="item" style="width:136px">OPLOSSINGEN</a>
    <a class="item" style="width:106px">BREACHES</a>
    <a class="item" style="width:84px">KENNIS</a>
    <a class="item" style="width:94px">KLANTEN</a>
    <a class="item" style="width:124px">OVER BRUNSVOLD</a>
    <div class="search"><svg width="12" height="12" viewBox="0 0 12 12"><circle cx="5" cy="5" r="3.5" fill="none" stroke="#fff" stroke-width="1.6"/><line x1="7.5" y1="7.5" x2="11" y2="11" stroke="#fff" stroke-width="2"/></svg></div>
  </nav>

  <div class="abs hero">
    <div class="p1" role="img" aria-label="Photo of a businessman on the phone in front of office towers"></div>
    <div class="p2" role="img" aria-label="Photo of a financial line chart"></div>
    <div class="p3" role="img" aria-label="Photo of a smiling business team"></div>
    <div class="p4" role="img" aria-label="Silhouettes of two business people shaking hands"></div>
  </div>
  <div class="abs hero-shadow"></div>

  <main class="abs features">
    <article class="feature" style="width:252px">
      <h2>Wie <b>Brunsvold ?</b></h2>
      <div class="lead"><div class="icon" role="img" aria-label="Rising bar chart icon" style="background:linear-gradient(135deg,#1f7fd0,#2b2b2b)"></div>
        <p><em>The performance of your employees has a great influence</em> on the performance of your organization. A motivated employee puts go that extra mile. And reap the fruits of your customers!</p></div>
      <p class="body">If an employee is dissatisfied and leaves your organization, will cost you an average of two years' salary. Valuable knowledge (about your organization and your customers)</p>
      <a class="more on">Moreinfo[+]</a>
    </article>
    <article class="feature" style="width:245px">
      <h2>What <b>done wij ?</b></h2>
      <div class="lead"><div class="icon" role="img" aria-label="Illustration of a group of people" style="background:linear-gradient(135deg,#e59a2a,#4aa53a)"></div>
        <p><em>The performance of your employees has a great influence</em> on the performance of your organization. A motivated employee puts go that extra mile. And reap the fruits of your customers!</p></div>
      <p class="body">If an employee is dissatisfied and leaves your organization, will cost you an average of two years' salary. Valuable knowledge (about your organization and your customers)</p>
      <a class="more">Moreinfo[+]</a>
    </article>
    <article class="feature" style="flex:1">
      <h2>Wat is het <b>resultaat ?</b></h2>
      <div class="lead"><div class="icon" role="img" aria-label="Illustration of an orange feed block with glasses" style="background:linear-gradient(135deg,#f7a43a,#e0620e)"></div>
        <p><em>The performance of your employees has a great influence</em> on the performance of your organization. A motivated employee puts go that extra mile. And reap the fruits of your customers!</p></div>
      <p class="body">If an employee is dissatisfied and leaves your organization, will cost you an average of two years' salary. Valuable knowledge (about your organization and your customers)</p>
      <a class="more">Moreinfo[+]</a>
    </article>
  </main>

  <section class="abs trusted">
    <h3>Trusted By</h3>
    <div class="badges">
      <span style="width:44px;height:36px"></span>
      <span style="width:28px;height:36px;border-radius:4px"></span>
      <span style="width:76px;height:22px"></span>
      <span style="width:26px;height:36px;border-radius:50%"></span>
      <span style="width:84px;height:24px;background:#9a9a9a"></span>
      <span style="width:88px;height:18px;background:#222"></span>
      <span style="width:36px;height:38px"></span>
      <span style="width:52px;height:34px;background:#777"></span>
      <span style="width:56px;height:34px;border-radius:50%;background:#333"></span>
      <span style="width:46px;height:30px;background:#222"></span>
    </div>
  </section>

  <section class="abs news">
    <div class="col list">
      <div class="post"><h4>Doorgroi- en ontwikkeling smogelijlkheden in crisisijd <time>October 4th, 2012</time></h4><p>Lorem Ipsum is simply dummy text of the printing and typesetting industry</p></div>
      <div class="post"><h4>Doorgroi- en ontwikkeling smogelijlkheden in crisisijd <time>October 4th, 2012</time></h4><p>Lorem Ipsum is simply dummy text of the printing and typesetting industry</p></div>
      <div class="post"><h4>Doorgroi- en ontwikkeling smogelijlkheden in crisisijd <time>October 4th, 2012</time></h4><p>Lorem Ipsum is simply dummy text of the printing</p></div>
    </div>
    <div class="col video">
      <div class="player">
        <div class="title">Box Selection and Multi-Line Editing Demo</div>
        <svg class="abs" style="left:88px;top:48px" width="34" height="34" viewBox="0 0 34 34"><circle cx="17" cy="17" r="14.5" fill="none" stroke="#fff" stroke-width="2.5"/><path d="M13 10 L25 17 L13 24Z" fill="#fff"/></svg>
        <div class="abs" style="left:0;right:0;top:84px;text-align:center;font-size:6px">click to play</div>
        <div class="bar">▸ video options<br>▸ playlist (1)</div>
      </div>
      <div class="player-shadow"></div>
    </div>
    <div class="col tweets">
      <div class="tweet"><h4>Brunsvold has @Steadfast</h4><p>Expertise and a thorough system: a real specialist in <a>http://qk.ly/tR4m2</a> #goedwerkgeven#zorgnet</p></div>
      <div class="tweet"><h4>Brunsvold has @Steadfast</h4><p>Expertise and a thorough system: a real specialist in <a>http://qk.ly/tR4m2</a> #goedwerkgeven#zorgnet</p></div>
      <div class="tweet"><h4>Brunsvold has @Steadfast</h4><p>Expertise and a thorough system: a real specialist in <a>http://qk.ly/tR4m2</a> #goedwerkgeven#zorgnet</p></div>
    </div>
  </section>

  <footer>
    <div class="abs contact-bar">
      <span style="margin-right:8px">020-41 62 200 - CONTACT</span>
      <div class="social"><span></span><span></span><span></span><span></span></div>
      <div class="newsletter">Schrijf je in voor onze nieuwsbrief
        <div class="field"><svg width="14" height="14" viewBox="0 0 12 12"><circle cx="5" cy="5" r="3.5" fill="none" stroke="#888" stroke-width="1.4"/><line x1="7.5" y1="7.5" x2="11" y2="11" stroke="#888" stroke-width="1.8"/></svg></div>
      </div>
    </div>
    <div class="abs sitemap">
      <section style="width:170px"><h5>Wat <b>doen Wij</b></h5><ul>
        <li>Why employee survey?</li><li>Method</li><li>Involvement</li><li>Effectiveness</li><li>Efficiency</li><li>Motivation of employees</li><li>Staff Satisfaction</li></ul></section>
      <section style="width:207px"><h5>Waar kunnen <b>we mee helpen</b></h5><ul>
        <li>Why internal customer survey?</li><li>Method</li><li>Internal customer satisfaction survey</li><li>Quality of staff departments</li><li>Internal collaboration research specifically</li><li>Project Evaluation</li><li>Studies</li><li>Price Information</li></ul></section>
      <section style="width:191px"><h5>Ruime <b>evering in</b></h5><ul>
        <li>Brunsvold in brief</li><li>Brunsvold in society</li><li>Mission, vision and strategy</li><li>Organogram</li><li>Directions</li><li>Satisfied employees</li><li>Satisfied customers</li><li>The National Satisfaction Index</li></ul></section>
      <section style="flex:1"><h5>Meer <b>over ons</b></h5><ul>
        <li>Willingness to change</li><li>Gradient Resistance</li><li>Failure Resistance</li><li>Vitality</li><li>Work Atmosphere</li><li>Questionnaire for employee satisfaction</li><li>Sample Employee Satisfaction</li><li>Survey of staff satisfaction</li></ul></section>
    </div>
    <div class="abs legal"><span>© 2012 Brunsvold. Employee and customer surveys</span><span>Privacy Policy &nbsp;&nbsp;| &nbsp;&nbsp;Terms and Conditions</span></div>
  </footer>

</div>
</body>
</html>
```